Mobile Repair Service on location needs a Web Design

We are starting a new mobile device repair service called Gadget Haven and our website needs a design!

Hello Designers!
First, we'd like to make clear this is more than a simple web design contest, we want the designers to create an idea. We want someone who can create the whole theme of the service's we provide. We want someone that can help design our visual branding, help us communicate a sentiment. And we are willing to pay for that.

Who are we?
Our company is based in Rotterdam, the Netherlands. We provide different services for all kinds of electronic devices. The kind of services we provide are, among other things, installations of hardware and software and the repair of broken or malfunctioning devices.
We are starting a new service that offers mobile device repairs on location, be it at the home of our customers, their office, or any other place. Just give us the address and we will come to you for the repair job. This is also our main USP. We have multiple skilled engineers who drive trough the country on a daily basis and can be on location within a working day. Repair is done immediately onsite while the customer waits. At this stage we will start with the smartphone product-group within the mobile devices. In a second phase we might also add tablets.
People don't want to be without their phone for weeks because of some parts that needed to be ordered by a repair center they had to sent their phone to. We offer a fully functional mobile repair center in the form of specially customized vans. These vans have all the tools and utilities needed by our engineers to safely repair your mobile device. Your phone is being repaired directly in front of you, the next business-day, on a location you desire.

For this new service we are creating a website called Gadget Haven. The website needs a story and matching design and this is where you come in. We are not looking for a simple template design we can get from any place. We need a story. We want you to create an idea, build a unique theme or vision that helps sell the product/service. This goes beyond the design of the website. We need the whole package, the design you are creating needs to have returning elements like icons, color use, images, maybe even characters etc. You name it! There needs to be a common thread in the design so we can reuse elements in, for example, the email templates, the work order or receipt we give to our customers (we may contact the winner of the contest to design these for us as well!).

The name 'Gadget Haven' is chosen. Haven (short for rehabilitate) has a bold and playful tone to it and the design needs to reflect the name. So we're looking for a somewhat playful and cheeky design. Definitely not too serious and definitely modern. We already got a logo that we love and that fit's this description (see attached design documents for the logo). It's bold, powerful and fun. Our web design needs to reflect this as well and has to fit in with our logo.
We would really like it if the design somehow incorporates elements that highlight our unique selling points (repairs on location, we come to you etc.). We would really like some form of story telling in the design. Think clumsy people breaking their phones. Teenagers in tears because they have no access to their friends. People nowadays have the need to always be 'connected'. What happens when your phone is broken or malfunctioning? We're handling tech, we are nerds and a little bit weird, but we're professionals and here to help you with your problem. The sentiment Wire Troop tries to communicate is something we really like. We're looking for fresh idea's, anything goes!

In an overview all Unique Selling Points of the Gadget haven service:
- Professional service on location. Don’t ship to us we will come to you!
- Clear pricing upfront. No hidden cost.
- Next business-day repair.
- Backed by a professional call center open 12 hours a day and open on a Saturday as well
- Backed by a professional repair center with more then 12 years of experience
- Repair is done by certified engineers
- 1 year warranty on the repair

The process:
The main function of our website will be for customers to make a repair request. A customer will visit our website and can make a repair request immediately by going through a 'request-order-flow'. In this flow he or she will need to fill in some forms and can select wich type/model/brand of mobile device he or she has and what parts need to be repaired. After a request is placed we will call the customer back (within an hour) for a short intake and to set a date/time and location. Our engineer will meet the customer at the specified location and will repair the device onsite in one of our mobile repair centers, which is a specialized van equipped with all the tools needed for device restorations.
So in short the steps are:
- Choose your device and repair job
- Place the order
- Get a callback within the hour
- Set date and location
- We will come to you.

Website functionality:
Our website is our main form of communication. So the sentiment we want to communicate needs be reflected in the design. We need a main/front page designed (preferably a long scrolling page design) containing:
1. Customers will be able to request a repair job directly on our website. So there will need to be a prominent button/link at the top of our main page that will bring the customer to this 'request-order-flow'. This is the main flow which needs to be full focus on the front page. All other items are secondary.
2. The general information of who we are and what we do, and why the customer should choose us. Preferably in short bullet-point type keywords/sentences with icons or other visual cues. See our unique selling points to get an idea of the information that will be displayed here.
3. There needs to be a section that will explain the process (see above) of a repair request step-by- step, again in brief short key sentences and with (custom) icons.
4. There needs to be a section that explains to the customer he/she can always contact us if they are not sure what the problem is with their device, and for this reason are not sure what repair request they should order.
5. We want to implement some functionality that display customer ratings or customer reviews. So there needs to be room for some kind of widget of plugin we're going to implement which shows these reviews.
6. A 'For business section' where we will explain all the options we provide for corporate clients.
7. Social media links.
8. There needs to be a menu with buttons that leads to the all sections described in the previous points.

For now, we need a design for our front page. In the second phase, when we have picked our winner, we may ask the winner to design the page(s) for our request workflow as well.

EDIT:
Finally, we have a very specific order in mind for the different segments of our website. We would like you to add some more segments that were not in our original brief as well:

1. Top header with order/request button. (should instantly make clear our main USP, we do repairs on location)
2. Our process
3. Our unique selling points / why choose us
4. The kind of repairs we do (broken screens, broken batteries, water damage, broken camera's, no sound etc.)
5. A 'meet our team' section, where we introduce some of our engineers
6. A 'contact us for any questions' section/
7. Testimonials/user reviews
8. A section where we show key performance indicators
9. 'For businesses' sections
10.'Subscribe for newsletter' field
11. Social media buttons

Industry/Entity Type

It Service

Number of Pages Required

1 page

Font styles to use
Sans Serif

Requirements
Must have
• a main/front page, design only
• custom icons/images for banners, adverts online and in print (high res)
Nice to have
• Storytelling in our design.
• Design that fits with our brand new logo.
• Elements like icons to have a flat design.
• Keep in mind that the website will need to be responsive when designing! (Ideally provide an example of the mobile design as well)
• Create a fun and trustworthy feeling.

```html
<!DOCTYPE html>
<html lang="en">
<head>
<meta charset="utf-8">
<title>Gadget Haven – Mobile Repair On Location</title>
<link rel="stylesheet" href="https://fonts.googleapis.com/css2?family=Raleway:wght@300;400;500;600;700;800&display=swap">
<style>
:root{
  --orange:#f26522;
  --orange-light:#ff8a3d;
  --ink:#1e1e1e;
  --text:#666;
  --muted:#8a8a8a;
  --lavender:#e4e2f0;
  --ring:#c9c6e4;
  --footer:#17181b;
  --white:#fff;
}
*{box-sizing:border-box;margin:0;padding:0}
html,body{width:1200px;height:3797px;overflow:hidden}
body{font-family:"Raleway",Arial,sans-serif;color:var(--ink);background:var(--white);position:relative}
.btn{display:inline-block;background:var(--orange);color:var(--white);border-radius:20px;font-size:14px;font-weight:500;padding:0 28px;line-height:34px;white-space:nowrap}

/* header */
.site-header{position:absolute;left:0;top:0;width:1200px;height:114px;background:var(--white)}
.brand{position:absolute;left:86px;top:30px;display:flex;align-items:center;gap:12px}
.brand-dot{width:50px;height:50px;border-radius:50%;background:var(--orange)}
.brand-name{font-size:24px;font-weight:800;color:var(--ink);line-height:1;letter-spacing:.5px}
.main-nav{position:absolute;left:400px;top:46px;width:565px;display:flex;justify-content:space-between;font-size:13px;color:#333;white-space:nowrap}
.main-nav .active{color:var(--orange)}
.header-cta{position:absolute;left:987px;top:36px;width:132px;text-align:center;padding:0;line-height:38px;font-size:14px}

/* hero */
.hero{position:absolute;left:0;top:114px;width:1200px;height:600px;background:linear-gradient(#efeeef,#dedcdd);clip-path:polygon(0 0,100% 0,100% 82%,0 100%);overflow:hidden}
.hero-photo{position:absolute;left:0;top:280px;width:1200px;height:320px;background:linear-gradient(180deg,#dcdadb 0%,#b9a79b 30%,#6f5a4f 60%,#4b4f5e 100%)}
.hero h1{position:absolute;left:0;width:1200px;text-align:center;top:48px;font-size:44px;font-weight:400;color:var(--orange)}
.hero h2{position:absolute;left:0;width:1200px;text-align:center;top:100px;font-size:44px;font-weight:600;color:var(--ink)}
.hero p{position:absolute;left:170px;width:860px;text-align:center;top:170px;font-size:16px;line-height:30px;color:#444}
.hero .btn{position:absolute;left:532px;top:244px}

/* intro columns */
.intro{position:absolute;left:0;top:734px;width:1200px;height:456px}
.intro-col{position:absolute;top:0;width:330px;text-align:center}
.intro-col svg{display:block;margin:24px auto 0}
.intro-col h3{margin-top:12px;font-size:26px;font-weight:400;line-height:30px}
.intro-col h3 strong{display:block;font-weight:700}
.intro-col p{margin-top:18px;font-size:13px;line-height:24px;color:var(--text)}
.intro-col .btn{margin-top:22px}
.intro-divider{position:absolute;top:100px;width:1px;height:240px;background:#ddd}

/* services */
.services{position:absolute;left:0;top:1190px;width:1200px;height:562px;background:linear-gradient(120deg,#f26522 0%,#ff8b40 45%,#f06a28 100%)}
.section-title{position:absolute;left:0;width:1200px;text-align:center;font-size:30px;font-weight:300;line-height:36px}
.section-title strong{display:block;font-weight:700}
.services .section-title{top:62px;color:var(--white)}
.rule{position:absolute;left:580px;width:40px;height:3px;background:var(--orange)}
.services .rule{background:var(--white);top:146px}
.usp{position:absolute;top:200px;width:150px;text-align:center;color:var(--white)}
.usp-ring{width:120px;height:120px;margin:0 auto;border-radius:50%;background:var(--ring);display:flex;align-items:center;justify-content:center}
.usp-core{width:90px;height:90px;border-radius:50%;background:#3b3c44;display:flex;align-items:center;justify-content:center}
.usp-stem{width:2px;height:38px;background:#3b3c44;margin:0 auto}
.usp-dot{width:14px;height:14px;border-radius:50%;background:#3b3c44;margin:0 auto}
.usp p{margin-top:16px;font-size:14px;line-height:19px}
.usp p strong{font-weight:700}
.usp p span{font-size:12px}

/* process */
.process{position:absolute;left:0;top:1752px;width:1200px;height:578px}
.process .section-title{top:58px}
.process .rule{top:142px}
.step{position:absolute;top:215px;width:190px;text-align:center}
.step-art{width:120px;height:165px;margin:0 auto;border-radius:10px;background:linear-gradient(#f4f4f4,#dedede)}
.step h4{margin-top:26px;font-size:15px;font-weight:400;color:var(--orange);line-height:21px}
.step p{margin-top:12px;font-size:12px;line-height:18px;color:var(--muted)}

/* contact band */
.help{position:absolute;left:0;top:2330px;width:1200px;height:450px;background:linear-gradient(90deg,#fbf6ee 0%,#f5ead9 60%,#e9d2b4 100%)}
.help-photo{position:absolute;left:734px;top:0;width:466px;height:450px;background:linear-gradient(100deg,#f5ead9 0%,#d8b99a 40%,#9a7d66 100%)}
.help .lead{position:absolute;left:80px;top:92px;width:640px;font-size:28px;line-height:34px;color:var(--orange);font-weight:400}
.help .reassure{position:absolute;left:80px;top:232px;width:640px;font-size:29px;line-height:36px;font-weight:700}
.help .btn{position:absolute;left:80px;top:327px}

/* testimonials */
.testimonials{position:absolute;left:0;top:2780px;width:1200px;height:405px}
.testimonials .section-title{top:60px}
.testimonials .rule{top:146px}
.review{position:absolute;top:200px;width:520px;height:140px}
.avatar{position:absolute;left:0;top:0;width:140px;height:140px;border-radius:50%;border:6px solid var(--orange);background:linear-gradient(#e8d7c8,#b6968a)}
.quote{position:absolute;left:160px;top:28px;width:360px;font-size:12px;line-height:20px;color:var(--muted)}
.quote::before{content:"\201C";position:absolute;left:-22px;top:-10px;font-size:40px;color:var(--ink);font-family:Georgia,serif}
.quote .close{font-size:30px;color:var(--ink);font-family:Georgia,serif;vertical-align:-12px}
.quote cite{display:block;margin-top:14px;font-style:normal;color:var(--orange)}

/* business */
.business{position:absolute;left:0;top:3185px;width:1200px;height:213px;background:var(--lavender)}
.business h3{position:absolute;left:128px;top:70px;width:120px;text-align:center;font-size:28px;font-weight:400;line-height:34px}
.business h3 strong{display:block;font-weight:700}
.business .divider{position:absolute;left:278px;top:50px;width:1px;height:120px;background:#aaa}
.business h4{position:absolute;left:312px;top:46px;font-size:30px;font-weight:400;color:#333}
.business ul{position:absolute;left:312px;top:98px;list-style:none;font-size:14px;font-weight:700;color:var(--orange);line-height:27px}
.business li::before{content:"\2022";margin-right:8px}

/* footer */
.site-footer{position:absolute;left:0;top:3398px;width:1200px;height:344px;background:var(--footer);color:#ddd}
.f-col{position:absolute;top:72px}
.f-col h5{font-size:17px;font-weight:400;color:var(--orange);padding-bottom:10px;border-bottom:1px solid #444;width:210px}
.f-col ul{list-style:none;margin-top:16px;font-size:13px;line-height:22px}
.f-col ul.links li::before{content:"\203A";margin-right:8px}
.f-col .row{display:flex;gap:10px;align-items:flex-start;font-size:13px;line-height:18px;margin-top:16px}
.f-col .freecall{color:var(--orange)}
.f-col p{margin-top:16px;font-size:13px;line-height:18px;width:230px}
.f-input{margin-top:14px;width:200px;height:26px;background:var(--white);font-size:11px;color:#999;padding:6px 10px}
.f-sub{margin-top:14px;display:inline-block;background:var(--orange);color:var(--white);font-size:12px;padding:4px 12px}
.social li{display:flex;align-items:center;gap:12px;margin-bottom:12px}
.social .sq{width:22px;height:22px;background:#3a6fb5}
.copyright{position:absolute;left:0;top:3742px;width:1200px;height:55px;background:var(--orange);color:var(--white);text-align:center;font-size:12px;line-height:55px}
</style>
</head>
<body>

<header class="site-header">
  <div class="brand"><span class="brand-dot"></span><span class="brand-name">Gadget Haven</span></div>
  <nav class="main-nav">
    <span class="active">Home</span><span>Who We Are</span><span>What We Do</span><span>Our Process</span><span>Pricing</span><span>Testimonials</span><span>Our Clients</span>
  </nav>
  <span class="btn header-cta">Contact Us</span>
</header>

<section class="hero">
  <div class="hero-photo" role="img" aria-label="Photo of four young friends sitting against a wall using their phones"></div>
  <h1>Best Mobile Repair Service</h1>
  <h2>At Any Time In Anywhere</h2>
  <p>We are starting a new service that offers mobile device repairs on location, be it at the home of our customers, their office, or any other place. Just give us the address and we will come to you for the repair job.</p>
  <span class="btn">Call Now</span>
</section>

<section class="intro">
  <div class="intro-col" style="left:68px">
    <svg width="50" height="46" viewBox="0 0 50 46"><circle cx="25" cy="11" r="8" fill="#f26522"/><circle cx="9" cy="20" r="6" fill="#f26522"/><circle cx="41" cy="20" r="6" fill="#f26522"/><path d="M11 44c0-10 6-16 14-16s14 6 14 16z" fill="#f26522"/></svg>
    <h3>Who <strong>We Are</strong></h3>
    <p>Our company is based in Rotterdam, the Netherlands. We provide different services for all kinds of electronic devices. The kind of services we provide are, among other things, installations of hardware and software and the repair of broken or malfunctioning devices.</p>
    <span class="btn">Read More</span>
  </div>
  <div class="intro-divider" style="left:418px"></div>
  <div class="intro-col" style="left:435px">
    <svg width="30" height="46" viewBox="0 0 30 46"><rect x="2" y="2" width="26" height="42" rx="4" fill="none" stroke="#f26522" stroke-width="3"/><rect x="7" y="8" width="16" height="26" fill="#f26522"/><circle cx="15" cy="39" r="2" fill="#f26522"/></svg>
    <h3>What <strong>We Do</strong></h3>
    <p>We are starting a new service that offers mobile device repairs on location, be it at the home of our customers, their office, or any other place. Just give us the address and we will come to you for the repair job. We offer a fully functional mobile repair center in the form of specially customized vans.</p>
    <span class="btn">Read More</span>
  </div>
  <div class="intro-divider" style="left:785px"></div>
  <div class="intro-col" style="left:802px">
    <svg width="40" height="46" viewBox="0 0 40 46"><path d="M14 6a4 4 0 0 1 8 0v16l10 3c4 1 5 4 4 8l-3 11H16L6 30c-2-3 2-6 5-4l3 3z" fill="#222"/><circle cx="18" cy="5" r="3" fill="#f26522"/></svg>
    <h3>Why <strong>Choose Us</strong></h3>
    <p>We have multiple skilled engineers who drive trough the country on a daily basis and can be on location within a working day. Repair is done immediately onsite while the customer waits. Your phone is being repaired directly in front of you, the next business-day, on a location you desire.</p>
    <span class="btn">Read More</span>
  </div>
</section>

<section class="services">
  <h2 class="section-title">Our <strong>Services</strong></h2>
  <div class="rule"></div>
  <div class="usp" style="left:69px"><div class="usp-ring"><div class="usp-core"><svg width="40" height="40" viewBox="0 0 40 40"><circle cx="24" cy="7" r="4" fill="#fff"/><path d="M20 13l-7 8 5 3-4 12M20 13l5 9 7 2M20 24l6 12" stroke="#fff" stroke-width="3" fill="none" stroke-linecap="round"/></svg></div></div><div class="usp-stem"></div><div class="usp-dot"></div><p><strong>Professional service</strong> on<br><span>location. Don't ship to us we will come to you!</span></p></div>
  <div class="usp" style="left:221px"><div class="usp-ring"><div class="usp-core"><svg width="40" height="40" viewBox="0 0 40 40"><circle cx="20" cy="20" r="13" fill="none" stroke="#fff" stroke-width="3"/><text x="20" y="27" text-anchor="middle" fill="#fff" font-size="18" font-family="Raleway,sans-serif" font-weight="700">$</text></svg></div></div><div class="usp-stem"></div><div class="usp-dot"></div><p><strong>Clear pricing upfront.</strong><br>No hidden cost.</p></div>
  <div class="usp" style="left:373px"><div class="usp-ring"><div class="usp-core"><svg width="40" height="40" viewBox="0 0 40 40"><path d="M12 6l6 7-3 4c2 4 5 7 9 9l4-3 7 6-4 5C20 34 6 20 6 10z" fill="#fff"/></svg></div></div><div class="usp-stem"></div><div class="usp-dot"></div><p><strong>Backed by a professional call center</strong> <span>open 12 hours a day and open on a Saturday as well.</span></p></div>
  <div class="usp" style="left:525px"><div class="usp-ring"><div class="usp-core"><svg width="40" height="40" viewBox="0 0 40 40"><rect x="6" y="9" width="28" height="25" rx="3" fill="none" stroke="#fff" stroke-width="3"/><path d="M6 16h28M13 5v7M27 5v7" stroke="#fff" stroke-width="3"/><rect x="12" y="21" width="5" height="5" fill="#fff"/><rect x="22" y="21" width="5" height="5" fill="#fff"/></svg></div></div><div class="usp-stem"></div><div class="usp-dot"></div><p><strong>Next business-day</strong><br><span>repair.</span></p></div>
  <div class="usp" style="left:677px"><div class="usp-ring"><div class="usp-core"><svg width="40" height="40" viewBox="0 0 40 40"><path d="M8 32L28 12M12 8l20 24" stroke="#fff" stroke-width="4" stroke-linecap="round"/><circle cx="30" cy="10" r="5" fill="none" stroke="#fff" stroke-width="3"/></svg></div></div><div class="usp-stem"></div><div class="usp-dot"></div><p><strong>Backed by a professional repair center</strong> <span>with more then 12 years of experience come to you!</span></p></div>
  <div class="usp" style="left:829px"><div class="usp-ring"><div class="usp-core"><svg width="40" height="40" viewBox="0 0 40 40"><circle cx="13" cy="13" r="5" fill="#fff"/><circle cx="27" cy="13" r="5" fill="#fff"/><path d="M4 32c0-7 4-11 9-11s9 4 9 11zM18 32c0-7 4-11 9-11s9 4 9 11z" fill="#fff"/></svg></div></div><div class="usp-stem"></div><div class="usp-dot"></div><p><strong>Repair is done by</strong> <span>certified engineers.</span></p></div>
  <div class="usp" style="left:981px"><div class="usp-ring"><div class="usp-core"><svg width="40" height="40" viewBox="0 0 40 40"><circle cx="20" cy="15" r="10" fill="none" stroke="#fff" stroke-width="3"/><path d="M14 24l-4 12 6-3 4 5 2-12M26 24l4 12-6-3" fill="#fff"/></svg></div></div><div class="usp-stem"></div><div class="usp-dot"></div><p><strong>1 year warranty</strong><br><span>on the repair.</span></p></div>
</section>

<section class="process">
  <h2 class="section-title">Our <strong>Process</strong></h2>
  <div class="rule"></div>
  <div class="step" style="left:75px"><div class="step-art" role="img" aria-label="Cartoon engineer choosing a device"></div><h4>Choose your device<br>and repair job</h4><p>Suspendisse iaculis elit nec ornare pellentes. Donec lacinia lectus malesuada.</p></div>
  <div class="step" style="left:290px"><div class="step-art" role="img" aria-label="Cartoon engineer placing the order"></div><h4>Place the<br>order</h4><p>Suspendisse iaculis elit nec ornare pellentes. Donec lacinia lectus malesuada.</p></div>
  <div class="step" style="left:505px"><div class="step-art" role="img" aria-label="Cartoon engineer waiting by a clock for the callback"></div><h4>Get a callback within<br>the hour</h4><p>Suspendisse iaculis elit nec ornare pellentes. Donec lacinia lectus malesuada.</p></div>
  <div class="step" style="left:720px"><div class="step-art" role="img" aria-label="Cartoon engineer holding a date and location sign"></div><h4>Set date and<br>location</h4><p>Suspendisse iaculis elit nec ornare pellentes. Donec lacinia lectus malesuada.</p></div>
  <div class="step" style="left:935px"><div class="step-art" role="img" aria-label="Cartoon engineer arriving at the customer"></div><h4>We will come<br>to you</h4><p>Suspendisse iaculis elit nec ornare pellentes. Donec lacinia lectus malesuada.</p></div>
</section>

<section class="help">
  <div class="help-photo" role="img" aria-label="Photo of a smiling woman with glasses talking on her phone"></div>
  <p class="lead">You are not sure what the problem is with their device, and for this reason you are not sure what repair request they should order.</p>
  <p class="reassure">Dont Worry, You can always contact us whatever the problem you have.</p>
  <span class="btn">Contact Us</span>
</section>

<section class="testimonials">
  <h2 class="section-title">Clients' <strong>Testimonials</strong></h2>
  <div class="rule"></div>
  <div class="review" style="left:82px">
    <div class="avatar" role="img" aria-label="Portrait of client Mira Sen"></div>
    <p class="quote">Donec turpis turpis, dapibus sed turpis vel, condimentum ultricies sem leo magna condimentum nulla. <span class="close">&rdquo;</span><cite>- Mira Sen</cite></p>
  </div>
  <div class="review" style="left:614px">
    <div class="avatar" role="img" aria-label="Portrait of client Arlo Finch"></div>
    <p class="quote">Donec turpis turpis, dapibus sed turpis vel, condimentum ultricies sem leo magna condimentum nulla. <span class="close">&rdquo;</span><cite>- Arlo Finch</cite></p>
  </div>
</section>

<section class="business">
  <h3>For <strong>Businees</strong></h3>
  <div class="divider"></div>
  <h4>The services we provide for corporate clients are-</h4>
  <ul>
    <li>In nec orci at diam sollicitudin mollis.</li>
    <li>Nunc venenatis ligula id purus varius, quis dapibus erat auctor.</li>
    <li>Suspendisse in diam vitae ex commodo commodo.</li>
  </ul>
</section>

<footer class="site-footer">
  <div class="f-col" style="left:84px;width:200px">
    <h5>Quick Links</h5>
    <ul class="links"><li>Home</li><li>Who We Are</li><li>What We Do</li><li>Our Process</li><li>Pricing</li><li>Testimonials</li><li>Our Clients</li><li>Contact Us</li></ul>
  </div>
  <div class="f-col" style="left:304px">
    <h5>Contact Information</h5>
    <div class="row"><svg width="12" height="16" viewBox="0 0 12 16"><path d="M6 0a6 6 0 0 1 6 6c0 4-6 10-6 10S0 10 0 6a6 6 0 0 1 6-6z" fill="#ddd"/><circle cx="6" cy="6" r="2" fill="#17181b"/></svg><span>Harbour Lane 12<br>3011 AB Rotterdam<br>PO Box 4521 Rotterdam</span></div>
    <div class="row"><svg width="12" height="14" viewBox="0 0 14 14"><path d="M3 0l3 3-2 2c1 2 3 4 5 5l2-2 3 3-2 3C6 14 0 8 0 3z" fill="#f26522"/></svg><span class="freecall">Freecall 555 010 2040</span></div>
    <div class="row"><svg width="14" height="10" viewBox="0 0 14 10"><rect width="14" height="10" fill="#ddd"/><path d="M0 0l7 6 7-6" stroke="#17181b" fill="none"/></svg><span>info@gadgethaven.com</span></div>
  </div>
  <div class="f-col" style="left:640px">
    <h5>Newsletter Signup</h5>
    <p>Please enter your email address below to receive our FREE newsletter</p>
    <div class="f-input">Your Email ID</div>
    <span class="f-sub">Subscribe</span>
  </div>
  <div class="f-col" style="left:932px">
    <h5>Follow Us</h5>
    <ul class="social">
      <li><span class="sq"></span>Facepage</li>
      <li><span class="sq"></span>Linkpro</li>
      <li><span class="sq" style="background:#3aa9e0"></span>Chirper</li>
      <li><span class="sq" style="background:#2bb3a0"></span>Email</li>
    </ul>
  </div>
</footer>
<div class="copyright">Copyright 2017@gadgethaven.com. All Rights Are Reserved.</div>

</body>
</html>
```